Poster promoting concerts of the 20th anniversary season of the Harborlight Sinfonietta Chamber Ensem

We need a poster (template) to promote the concert season and individual concerts of the Harborlight Sinfonietta.
We present 8-10 programs avery season (oct - May)
the current info is on our website at www.theharborlightband.org. Imagery from the website can be used for the design.
IMPORTANT DETAILS:
This season the orchestra will celebrate its 20th anniversary.
Poster must be printable in both color and black / white
Poster must be readable from a distance
Poster size is 11x17 inch
Website is NOT representative of the graphic design as we are looking to update the site after the poster is created.

Requirements
Must have
• Poster must be printable in both color and black / white
• Poster must be readable from a distance
• Poster size is 11x17 inch
Nice to have
• Please see the files for the soloists.

```html
<!DOCTYPE html>
<html lang="en">
<head>
<meta charset="utf-8">
<title>Harborlight Sinfonietta – Season Poster</title>
<link rel="stylesheet" href="https://fonts.googleapis.com/css2?family=PT+Sans+Narrow:wght@400;700&display=swap">
<style>
  :root {
    --page-bg: #a8a8a8;
    --pin-fill: #2a68bb;
    --pin-ring: #ffffff;
    --card-fill: rgba(255,255,255,0.82);
    --card-text: #1b1b1b;
    --title-ink: #2a1a9c;
  }
  html, body {
    margin: 0;
    width: 1200px;
    height: 1176px;
    overflow: hidden;
    background: var(--page-bg);
  }
  .posters {
    display: flex;
    gap: 40px;
    padding: 171px 40px 0;
  }
  .poster {
    width: 540px;
    height: 834px;
    display: block;
    box-shadow: 0 6px 18px rgba(0,0,0,0.25);
    font-family: "PT Sans Narrow", "Arial Narrow", sans-serif;
  }
  .poster--mono { filter: grayscale(1); --title-ink: #4e4e4e; }
  .card { fill: var(--card-fill); }
  .card-text { font-size: 10.5px; fill: var(--card-text); }
  .card-text .date { font-weight: 700; }
  .card-text--bold { font-weight: 700; }
  .pin-ring { fill: var(--pin-ring); }
  .pin-core { fill: var(--pin-fill); }
  .pin-shadow { fill: #000; opacity: 0.55; }
  .pin-label { fill: #fff; text-anchor: middle; font-size: 10.5px; }
  .pin-label--mid { font-size: 12.5px; }
  .pin-label--large { font-size: 14px; }
  .pin-label--tiny { font-size: 6.5px; font-weight: 700; }
  .ensemble-name {
    font-weight: 700;
    font-size: 31px;
    fill: var(--title-ink);
    letter-spacing: -0.5px;
  }
</style>
</head>
<body>
<main class="posters">

  <!-- Colour edition -->
  <svg class="poster poster--color" viewBox="0 0 639 987" role="img" aria-label="Season poster, colour edition">
    <defs>
      <radialGradient id="a-sky" cx="0.48" cy="0.45" r="0.75">
        <stop offset="0" stop-color="#8db6e2"/>
        <stop offset="0.45" stop-color="#3b7dcb"/>
        <stop offset="1" stop-color="#0a4aa6"/>
      </radialGradient>
      <linearGradient id="a-strip" x1="0" x2="1">
        <stop offset="0" stop-color="#1c3f7a"/>
        <stop offset="0.3" stop-color="#4d86cf"/>
        <stop offset="0.55" stop-color="#22467e"/>
        <stop offset="0.8" stop-color="#6a9fe0"/>
        <stop offset="1" stop-color="#3d78c8"/>
      </linearGradient>
      <linearGradient id="a-crowd" x1="0" y1="0" x2="0" y2="1">
        <stop offset="0" stop-color="#1d55a6" stop-opacity="0"/>
        <stop offset="1" stop-color="#14448c" stop-opacity="0.55"/>
      </linearGradient>
      <linearGradient id="a-band" x1="0" y1="0" x2="0" y2="1">
        <stop offset="0" stop-color="#9a9a9a"/>
        <stop offset="0.1" stop-color="#d8d8d8"/>
        <stop offset="0.5" stop-color="#ececec"/>
        <stop offset="1" stop-color="#d2d2d2"/>
      </linearGradient>
      <filter id="a-soft"><feGaussianBlur stdDeviation="4"/></filter>
      <path id="a-pin" d="M0,75 C-8,56 -43,32 -43,0 A43,43 0 1 1 43,0 C43,32 8,56 0,75Z"/>
    </defs>

    <rect class="sky" width="639" height="852" fill="url(#a-sky)"/>
    <rect role="img" aria-label="Faint illustration of costumed musicians playing" x="0" y="520" width="639" height="332" fill="url(#a-crowd)"/>
    <rect role="img" aria-label="Strip of soloist portrait photographs" width="639" height="113" fill="url(#a-strip)"/>
    <rect class="bottom-band" y="852" width="639" height="135" fill="url(#a-band)"/>

    <rect class="card" x="78" y="258" width="230" height="76" rx="4"/>
    <text class="card-text" x="87" y="277"><tspan class="date">October 21</tspan><tspan x="87" dy="13.5">Elm Street Congregational Church, Westbrook</tspan><tspan class="date" x="87" dy="13.5">October 23</tspan><tspan x="87" dy="13.5">St. Anselm Church, Harborview</tspan></text>
    <g transform="translate(132,181)"><use href="#a-pin" class="pin-shadow" transform="translate(-7,-5)" filter="url(#a-soft)"/><use href="#a-pin" class="pin-ring"/><circle class="pin-core" r="36"/>
      <text class="pin-label" y="-8">MORAVEK,<tspan x="0" dy="12">WESTERHOLM,</tspan><tspan x="0" dy="12">HALDEN</tspan></text></g>

    <rect class="card" x="376" y="241" width="230" height="122" rx="4"/>
    <text class="card-text" x="385" y="260"><tspan class="date">November 4</tspan><tspan x="385" dy="13.5">Mainstage Arts Center, Westbrook</tspan><tspan class="date" x="385" dy="13.5">November 6</tspan><tspan x="385" dy="13.5">Larkspur Atheneum Museum of Art, Harborview</tspan><tspan class="date" x="385" dy="13.5">November 13</tspan><tspan x="385" dy="13.5">Ridgefield Arts Center, Millbrook</tspan><tspan class="date" x="385" dy="13.5">November 19</tspan><tspan x="385" dy="13.5">Beacon Arts Center, Port Haven</tspan></text>
    <g transform="translate(433,168)"><use href="#a-pin" class="pin-shadow" transform="translate(-7,-5)" filter="url(#a-soft)"/><use href="#a-pin" class="pin-ring"/><circle class="pin-core" r="36"/>
      <text class="pin-label" y="-1">VOLKORINSKY<tspan x="0" dy="13">ODALINE</tspan></text></g>

    <rect class="card" x="13" y="463" width="249" height="70" rx="4"/>
    <text class="card-text card-text--bold" x="22" y="482">December 9<tspan x="22" dy="13.5">Elm Street Congregational Church, Westbrook</tspan><tspan x="22" dy="13.5">December 10</tspan><tspan x="22" dy="13.5">St. Anselm Church, Harborview</tspan></text>
    <g transform="translate(70,388)"><use href="#a-pin" class="pin-shadow" transform="translate(-7,-5)" filter="url(#a-soft)"/><use href="#a-pin" class="pin-ring"/><circle class="pin-core" r="36"/>
      <text class="pin-label" y="-3">ITALIAN<tspan x="0" dy="13">MASTERWORKS</tspan></text></g>

    <rect class="card" x="277" y="420" width="249" height="70" rx="4"/>
    <text class="card-text" x="286" y="439"><tspan class="date">February 24</tspan><tspan x="286" dy="13.5">Elm Street Congregational Church, Westbrook</tspan><tspan class="date" x="286" dy="13.5">February 24 &amp; 25</tspan><tspan x="286" dy="13.5">St. Anselm Church, Harborview</tspan></text>
    <g transform="translate(336,346)"><use href="#a-pin" class="pin-shadow" transform="translate(-7,-5)" filter="url(#a-soft)"/><use href="#a-pin" class="pin-ring"/><circle class="pin-core" r="36"/>
      <text class="pin-label pin-label--tiny" y="-16">WESTERHOLM:<tspan x="0" dy="9">CONCERTO</tspan><tspan x="0" dy="9">FOR VIOLIN,</tspan><tspan x="0" dy="9">PIANO AND</tspan><tspan x="0" dy="9">STRINGS</tspan></text></g>

    <rect class="card" x="373" y="596" width="248" height="70" rx="4"/>
    <text class="card-text" x="382" y="615"><tspan class="date">March 24</tspan><tspan x="382" dy="13.5">Elm Street Congregational Church, Westbrook</tspan><tspan class="date" x="382" dy="13.5">March 25</tspan><tspan x="382" dy="13.5">St. Anselm Church, Harborview</tspan></text>
    <g transform="translate(430,521)"><use href="#a-pin" class="pin-shadow" transform="translate(-7,-5)" filter="url(#a-soft)"/><use href="#a-pin" class="pin-ring"/><circle class="pin-core" r="36"/>
      <text class="pin-label pin-label--mid" y="-1">MUSIC OF<tspan x="0" dy="15">J. R. BEALE</tspan></text></g>

    <rect class="card" x="39" y="681" width="156" height="70" rx="4"/>
    <text class="card-text" x="48" y="700"><tspan class="date">April 21</tspan><tspan x="48" dy="13.5">Holy Rood Church, Westbrook</tspan><tspan class="date" x="48" dy="13.5">April 23</tspan><tspan x="48" dy="13.5">St Brendan Cathedral, Harborview</tspan></text>
    <g transform="translate(95,608)"><use href="#a-pin" class="pin-shadow" transform="translate(-7,-5)" filter="url(#a-soft)"/><use href="#a-pin" class="pin-ring"/><circle class="pin-core" r="36"/>
      <text class="pin-label" y="-10" style="font-size:12px">BRANDT:<tspan x="0" dy="15">VIOLIN</tspan><tspan x="0" dy="15">CONCERTO</tspan></text></g>

    <rect class="card" x="242" y="694" width="199" height="134" rx="4"/>
    <text class="card-text card-text--bold" x="251" y="712">May 5<tspan x="251" dy="13.5">Mainstage</tspan><tspan x="251" dy="13.5">Arts Center, Westbrook</tspan><tspan x="251" dy="13.5">May 14</tspan><tspan x="251" dy="13.5">Ridgefield Arts Center, Millbrook</tspan><tspan x="251" dy="13.5">May 20</tspan><tspan x="251" dy="13.5">Larkspur Atheneum Museum of Art</tspan><tspan x="251" dy="13.5">May 21</tspan><tspan x="251" dy="13.5">Beacon Arts Center, Port Haven</tspan></text>
    <g transform="translate(298,621)"><use href="#a-pin" class="pin-shadow" transform="translate(-7,-5)" filter="url(#a-soft)"/><use href="#a-pin" class="pin-ring"/><circle class="pin-core" r="36"/>
      <text class="pin-label pin-label--large" y="-3">PELLARI:<tspan x="0" dy="17">TESSA</tspan></text></g>

    <text class="ensemble-name" x="22" y="922">HARBORLIGHT<tspan x="22" dy="23">SINFONIETTA CHAMBER</tspan><tspan x="22" dy="23">ENSEMBLE</tspan></text>
  </svg>

  <!-- Black and white edition -->
  <svg class="poster poster--mono" viewBox="0 0 639 987" role="img" aria-label="Season poster, black and white edition">
    <defs>
      <radialGradient id="b-sky" cx="0.48" cy="0.45" r="0.75">
        <stop offset="0" stop-color="#8db6e2"/>
        <stop offset="0.45" stop-color="#3b7dcb"/>
        <stop offset="1" stop-color="#0a4aa6"/>
      </radialGradient>
      <linearGradient id="b-strip" x1="0" x2="1">
        <stop offset="0" stop-color="#1c3f7a"/>
        <stop offset="0.3" stop-color="#4d86cf"/>
        <stop offset="0.55" stop-color="#22467e"/>
        <stop offset="0.8" stop-color="#6a9fe0"/>
        <stop offset="1" stop-color="#3d78c8"/>
      </linearGradient>
      <linearGradient id="b-crowd" x1="0" y1="0" x2="0" y2="1">
        <stop offset="0" stop-color="#1d55a6" stop-opacity="0"/>
        <stop offset="1" stop-color="#14448c" stop-opacity="0.55"/>
      </linearGradient>
      <linearGradient id="b-band" x1="0" y1="0" x2="0" y2="1">
        <stop offset="0" stop-color="#9a9a9a"/>
        <stop offset="0.1" stop-color="#d8d8d8"/>
        <stop offset="0.5" stop-color="#ececec"/>
        <stop offset="1" stop-color="#d2d2d2"/>
      </linearGradient>
      <filter id="b-soft"><feGaussianBlur stdDeviation="4"/></filter>
      <path id="b-pin" d="M0,75 C-8,56 -43,32 -43,0 A43,43 0 1 1 43,0 C43,32 8,56 0,75Z"/>
    </defs>

    <rect class="sky" width="639" height="852" fill="url(#b-sky)"/>
    <rect role="img" aria-label="Faint illustration of costumed musicians playing" x="0" y="520" width="639" height="332" fill="url(#b-crowd)"/>
    <rect role="img" aria-label="Strip of soloist portrait photographs" width="639" height="113" fill="url(#b-strip)"/>
    <rect class="bottom-band" y="852" width="639" height="135" fill="url(#b-band)"/>

    <rect class="card" x="78" y="258" width="230" height="76" rx="4"/>
    <text class="card-text" x="87" y="277"><tspan class="date">October 21</tspan><tspan x="87" dy="13.5">Elm Street Congregational Church, Westbrook</tspan><tspan class="date" x="87" dy="13.5">October 23</tspan><tspan x="87" dy="13.5">St. Anselm Church, Harborview</tspan></text>
    <g transform="translate(132,181)"><use href="#b-pin" class="pin-shadow" transform="translate(-7,-5)" filter="url(#b-soft)"/><use href="#b-pin" class="pin-ring"/><circle class="pin-core" r="36"/>
      <text class="pin-label" y="-8">MORAVEK,<tspan x="0" dy="12">WESTERHOLM,</tspan><tspan x="0" dy="12">HALDEN</tspan></text></g>

    <rect class="card" x="376" y="241" width="230" height="122" rx="4"/>
    <text class="card-text" x="385" y="260"><tspan class="date">November 4</tspan><tspan x="385" dy="13.5">Mainstage Arts Center, Westbrook</tspan><tspan class="date" x="385" dy="13.5">November 6</tspan><tspan x="385" dy="13.5">Larkspur Atheneum Museum of Art, Harborview</tspan><tspan class="date" x="385" dy="13.5">November 13</tspan><tspan x="385" dy="13.5">Ridgefield Arts Center, Millbrook</tspan><tspan class="date" x="385" dy="13.5">November 19</tspan><tspan x="385" dy="13.5">Beacon Arts Center, Port Haven</tspan></text>
    <g transform="translate(433,168)"><use href="#b-pin" class="pin-shadow" transform="translate(-7,-5)" filter="url(#b-soft)"/><use href="#b-pin" class="pin-ring"/><circle class="pin-core" r="36"/>
      <text class="pin-label" y="-1">VOLKORINSKY<tspan x="0" dy="13">ODALINE</tspan></text></g>

    <rect class="card" x="13" y="463" width="249" height="70" rx="4"/>
    <text class="card-text card-text--bold" x="22" y="482">December 9<tspan x="22" dy="13.5">Elm Street Congregational Church, Westbrook</tspan><tspan x="22" dy="13.5">December 10</tspan><tspan x="22" dy="13.5">St. Anselm Church, Harborview</tspan></text>
    <g transform="translate(70,388)"><use href="#b-pin" class="pin-shadow" transform="translate(-7,-5)" filter="url(#b-soft)"/><use href="#b-pin" class="pin-ring"/><circle class="pin-core" r="36"/>
      <text class="pin-label" y="-3">ITALIAN<tspan x="0" dy="13">MASTERWORKS</tspan></text></g>

    <rect class="card" x="277" y="420" width="249" height="70" rx="4"/>
    <text class="card-text" x="286" y="439"><tspan class="date">February 24</tspan><tspan x="286" dy="13.5">Elm Street Congregational Church, Westbrook</tspan><tspan class="date" x="286" dy="13.5">February 24 &amp; 25</tspan><tspan x="286" dy="13.5">St. Anselm Church, Harborview</tspan></text>
    <g transform="translate(336,346)"><use href="#b-pin" class="pin-shadow" transform="translate(-7,-5)" filter="url(#b-soft)"/><use href="#b-pin" class="pin-ring"/><circle class="pin-core" r="36"/>
      <text class="pin-label pin-label--tiny" y="-16">WESTERHOLM:<tspan x="0" dy="9">CONCERTO</tspan><tspan x="0" dy="9">FOR VIOLIN,</tspan><tspan x="0" dy="9">PIANO AND</tspan><tspan x="0" dy="9">STRINGS</tspan></text></g>

    <rect class="card" x="373" y="596" width="248" height="70" rx="4"/>
    <text class="card-text" x="382" y="615"><tspan class="date">March 24</tspan><tspan x="382" dy="13.5">Elm Street Congregational Church, Westbrook</tspan><tspan class="date" x="382" dy="13.5">March 25</tspan><tspan x="382" dy="13.5">St. Anselm Church, Harborview</tspan></text>
    <g transform="translate(430,521)"><use href="#b-pin" class="pin-shadow" transform="translate(-7,-5)" filter="url(#b-soft)"/><use href="#b-pin" class="pin-ring"/><circle class="pin-core" r="36"/>
      <text class="pin-label pin-label--mid" y="-1">MUSIC OF<tspan x="0" dy="15">J. R. BEALE</tspan></text></g>

    <rect class="card" x="39" y="681" width="156" height="70" rx="4"/>
    <text class="card-text" x="48" y="700"><tspan class="date">April 21</tspan><tspan x="48" dy="13.5">Holy Rood Church, Westbrook</tspan><tspan class="date" x="48" dy="13.5">April 23</tspan><tspan x="48" dy="13.5">St Brendan Cathedral, Harborview</tspan></text>
    <g transform="translate(95,608)"><use href="#b-pin" class="pin-shadow" transform="translate(-7,-5)" filter="url(#b-soft)"/><use href="#b-pin" class="pin-ring"/><circle class="pin-core" r="36"/>
      <text class="pin-label" y="-10" style="font-size:12px">BRANDT:<tspan x="0" dy="15">VIOLIN</tspan><tspan x="0" dy="15">CONCERTO</tspan></text></g>

    <rect class="card" x="242" y="694" width="199" height="134" rx="4"/>
    <text class="card-text card-text--bold" x="251" y="712">May 5<tspan x="251" dy="13.5">Mainstage</tspan><tspan x="251" dy="13.5">Arts Center, Westbrook</tspan><tspan x="251" dy="13.5">May 14</tspan><tspan x="251" dy="13.5">Ridgefield Arts Center, Millbrook</tspan><tspan x="251" dy="13.5">May 20</tspan><tspan x="251" dy="13.5">Larkspur Atheneum Museum of Art</tspan><tspan x="251" dy="13.5">May 21</tspan><tspan x="251" dy="13.5">Beacon Arts Center, Port Haven</tspan></text>
    <g transform="translate(298,621)"><use href="#b-pin" class="pin-shadow" transform="translate(-7,-5)" filter="url(#b-soft)"/><use href="#b-pin" class="pin-ring"/><circle class="pin-core" r="36"/>
      <text class="pin-label pin-label--large" y="-3">PELLARI:<tspan x="0" dy="17">TESSA</tspan></text></g>

    <text class="ensemble-name" x="22" y="922">HARBORLIGHT<tspan x="22" dy="23">SINFONIETTA CHAMBER</tspan><tspan x="22" dy="23">ENSEMBLE</tspan></text>
  </svg>

</main>
</body>
</html>
```